Marrowby Roofing & Exteriors Ltd

I would like to start a Chatterleaf page for business that outlines marrowby roofing . We have been in business since 2005 & have completed more than 5000 projects . Our company is area licensed, insured , covered by pqh , kfv member , journey man roofers , offer financing, zero down payment required , free quotes , serving red deer & area .

Please do not put years on the homepage.

Target Market(s)

Roofers in red deer & central Alberta

Industry/Entity Type

Roofing

Requirements
Must have
• Shingles , soffit , fascia , siding , gutters , roof repair , exterior painting , exterior washing .

```html
<!DOCTYPE html>
<html lang="en">
<head>
<meta charset="UTF-8">
<title>Marrowby Roofing &amp; Exteriors Ltd — Cover</title>
<link href="https://fonts.googleapis.com/css2?family=Raleway:wght@300;800;900&display=swap" rel="stylesheet">
<style>
  :root {
    --stage: #343434;
    --brand-red: #9b0f1c;
    --brand-red-deep: #86101a;
    --white: #ffffff;
    --sky-blue: #9cc3e6;
    --siding-navy: #3a4a5e;
    --lawn-green: #6f8f4a;
    --shingle-grey: #6d6f73;
    --stone-taupe: #8a7f74;
    --overcast: #c9d0d6;
  }
  * { margin: 0; padding: 0; box-sizing: border-box; }
  html, body {
    width: 1200px;
    height: 667px;
    overflow: hidden;
    background: var(--stage);
  }
  .cover {
    position: absolute;
    left: 0;
    top: 105px;
    width: 1200px;
    height: 456px;
    overflow: hidden;
    font-family: "Raleway", sans-serif;
  }
  .cover-art {
    position: absolute;
    inset: 0;
    width: 1200px;
    height: 456px;
  }
  .headline-block {
    position: absolute;
    left: 77px;
    top: 145px;
    width: 309px;
    color: var(--white);
  }
  .rule {
    height: 2px;
    background: var(--white);
  }
  .rule-bottom { margin-top: 12px; }
  .intro {
    font-weight: 300;
    font-size: 25px;
    line-height: 1;
    margin-top: 15px;
    letter-spacing: 0.2px;
  }
  .services {
    font-weight: 900;
    font-size: 31px;
    line-height: 36px;
    margin-top: 4px;
    letter-spacing: -0.2px;
  }
  .credentials {
    position: absolute;
    left: 77px;
    top: 358px;
    font-weight: 900;
    font-size: 17.5px;
    line-height: 1;
    color: var(--brand-red);
    letter-spacing: 0.2px;
    white-space: pre;
  }
</style>
</head>
<body>
  <main class="cover">
    <svg class="cover-art" viewBox="0 0 1200 456" xmlns="http://www.w3.org/2000/svg">
      <defs>
        <linearGradient id="redField" x1="0" y1="0" x2="0" y2="1">
          <stop offset="0" stop-color="#a3111f"/>
          <stop offset="1" stop-color="#930e1a"/>
        </linearGradient>
        <linearGradient id="photoTop" x1="0" y1="0" x2="0" y2="1">
          <stop offset="0" stop-color="#a9c9e6"/>
          <stop offset="0.5" stop-color="#3a4a5e"/>
          <stop offset="1" stop-color="#b7a892"/>
        </linearGradient>
        <linearGradient id="photoMid" x1="0" y1="0" x2="1" y2="0">
          <stop offset="0" stop-color="#6f8f4a"/>
          <stop offset="0.35" stop-color="#6d6f73"/>
          <stop offset="1" stop-color="#7ea050"/>
        </linearGradient>
        <linearGradient id="photoLow" x1="0" y1="0" x2="0" y2="1">
          <stop offset="0" stop-color="#3f86d8"/>
          <stop offset="0.45" stop-color="#8c7c6c"/>
          <stop offset="1" stop-color="#2a2a2a"/>
        </linearGradient>
        <linearGradient id="photoMain" x1="0" y1="0" x2="0" y2="1">
          <stop offset="0" stop-color="#c9d0d6"/>
          <stop offset="0.35" stop-color="#b7b8b8"/>
          <stop offset="0.55" stop-color="#8a7f74"/>
          <stop offset="0.8" stop-color="#b6aea3"/>
          <stop offset="1" stop-color="#3b3c3f"/>
        </linearGradient>
      </defs>

      <rect class="field-white" x="0" y="0" width="1200" height="456" fill="var(--white)"/>
      <polygon class="field-red" points="0,0 617,0 425,456 0,456" fill="url(#redField)"/>
      <polygon class="credential-band" points="0,351 487,351 474,382 0,382" fill="var(--white)"/>

      <polygon class="photo photo-main" role="img"
        aria-label="Photo: stone-clad bungalow with grey shingle roof, garage door and paved driveway"
        points="861,0 1200,0 1200,456 704,456" fill="url(#photoMain)"/>
      <polygon class="photo photo-top" role="img"
        aria-label="Photo: two-storey house with navy siding and a newly finished roof"
        points="618,1 857,1 808,147 556,147" fill="url(#photoTop)"/>
      <polygon class="photo photo-mid" role="img"
        aria-label="Photo: aerial view of a roof being re-shingled, surrounded by lawn"
        points="552,156 804,156 755,301 491,301" fill="url(#photoMid)"/>
      <polygon class="photo photo-low" role="img"
        aria-label="Photo: work bins parked in front of a house during a roofing job"
        points="488,310 752,310 701,454 426,454" fill="url(#photoLow)"/>
    </svg>

    <section class="headline-block">
      <div class="rule"></div>
      <p class="intro">We Specialize in</p>
      <h1 class="services">Residential,<br>Commercial &amp;<br>Industrial Roofing</h1>
      <div class="rule rule-bottom"></div>
    </section>

    <p class="credentials">BONDED   |   LICENSED   |   INSURED</p>
  </main>
</body>
</html>
```